BRANWELL LAW FIRM

Seeking a business logo and business card design incorporating the logo. We have an existing business card (attached), which we would like redesigned incorporating the new logo and existing text (front and back). Also, logo and business card should incorporate the same color scheme as on the attached. There are several employees who will need business cards; not sure how this is handled from a business card design standpoint . . . please contact me with any questions/concerns.

Please feel free to redesign front of business card. Branwell Law Firm must read Branwell Law Firm, P.C.

Back of business card should have the below address information towards the bottom of the card, so there is room for someone to write on the back. The address information on the back of the business cards is as follows:

Three Galton Court Plaza
2700 Marrow Boulevard, Suite 3040
Philadelphia, PA 19999
T: (215) 555.0143

68 Tilbury Avenue, 24th Floor
New York, NY 10099
T: (212) 555-0188

Industry/Entity Type

Business

Logo Text

BLF

```html
<!DOCTYPE html>
<html lang="en">
<head>
<meta charset="utf-8">
<title>Branwell Law Firm, P.C. — Business Card</title>
<link href="https://fonts.googleapis.com/css2?family=Montserrat:wght@400;600;700&display=swap" rel="stylesheet">
<style>
  :root {
    --navy: #2c3a4e;
    --card: #ffffff;
    --ink: #1f2530;
    --backdrop: #e6e6e4;
  }
  html, body {
    margin: 0;
    padding: 0;
    width: 1200px;
    height: 873px;
    overflow: hidden;
    background: var(--backdrop);
  }
  .canvas {
    position: relative;
    width: 1200px;
    height: 873px;
    display: flex;
    align-items: center;
    justify-content: center;
    gap: 40px;
    font-family: "Montserrat", sans-serif;
  }
  .card {
    position: relative;
    width: 520px;
    height: 297px;
    background: var(--card);
    box-shadow: 0 2px 10px rgba(0,0,0,0.12);
    box-sizing: border-box;
    overflow: hidden;
  }
  .brand {
    display: flex;
    align-items: center;
    gap: 8px;
    color: var(--navy);
    font-weight: 700;
    letter-spacing: 0.02em;
    line-height: 1;
  }
  .brand__square {
    display: inline-block;
    background: var(--navy);
  }
  .firm-name {
    margin: 0;
    color: var(--navy);
    font-weight: 600;
    letter-spacing: 0.12em;
    text-transform: uppercase;
    line-height: 1;
  }

  /* Back: brand at top, addresses toward the bottom */
  .card--back .brand-lockup {
    position: absolute;
    right: 34px;
    top: 30px;
    display: flex;
    flex-direction: column;
    align-items: flex-end;
    gap: 7px;
  }
  .card--back .brand { font-size: 30px; }
  .card--back .brand__square { width: 14px; height: 14px; }
  .card--back .firm-name { font-size: 8px; }
  .card--back .address-block {
    position: absolute;
    left: 34px;
    bottom: 32px;
    margin: 0;
    font-style: normal;
    font-size: 14px;
    line-height: 19px;
    letter-spacing: 0.04em;
    text-transform: uppercase;
    color: var(--ink);
  }
  .card--back .office + .office { margin-top: 10px; }
  .card--back .office p { margin: 0; }
  .card--back .edge-band {
    position: absolute;
    left: 0;
    right: 0;
    bottom: 0;
    height: 11px;
    background: var(--navy);
  }

  /* Front: name + brand */
  .card--front .holder-name {
    position: absolute;
    left: 30px;
    top: 26px;
    margin: 0;
    font-size: 15px;
    font-weight: 600;
    letter-spacing: 0.06em;
    text-transform: uppercase;
    color: var(--ink);
  }
  .card--front .brand-lockup {
    position: absolute;
    left: 50%;
    top: 56%;
    transform: translate(-50%, -50%);
    display: flex;
    flex-direction: column;
    align-items: center;
    gap: 12px;
  }
  .card--front .brand { font-size: 62px; }
  .card--front .brand__square { width: 26px; height: 26px; }
  .card--front .firm-name { font-size: 11px; }
</style>
</head>
<body>
<main class="canvas">
  <section class="card card--back" aria-label="Business card back">
    <div class="brand-lockup">
      <div class="brand"><span class="brand__square"></span>BLF</div>
      <p class="firm-name">Branwell Law Firm, P.C.</p>
    </div>
    <address class="address-block">
      <div class="office">
        <p>Three Galton Court Plaza</p>
        <p>2700 Marrow Boulevard, Suite 3040</p>
        <p>Philadelphia, PA 19999</p>
        <p>T: (215) 555.0143</p>
      </div>
      <div class="office">
        <p>68 Tilbury Avenue, 24th Floor</p>
        <p>New York, NY 10099</p>
        <p>T: (212) 555-0188</p>
      </div>
    </address>
    <div class="edge-band"></div>
  </section>

  <section class="card card--front" aria-label="Business card front">
    <h1 class="holder-name">Martin R. Oakes</h1>
    <div class="brand-lockup">
      <div class="brand"><span class="brand__square"></span>BLF</div>
      <p class="firm-name">Branwell Law Firm, P.C.</p>
    </div>
  </section>
</main>
</body>
</html>
```